BRVO2020 Save the date post card

Take the look and feel of the logo you designed and create a save the date postcard. 7L" by 5"H - print ready file with crop marks and bleeds.

Colors

Designer to choose colors to be used in the design.

Requirements
Must have
• The logo somewhere on the card.
• The following text:
• Save the Date
• June 1 - 4
• brvosummitfold.ca
• Stronger Always: Gather. Spark. Flourish.
Nice to have
• The following text:
• Vision: The vision of the BRVO 2020 conference is to improve patient care by bringing together the Canadian Emergency Medicine community.
• Learning Objectives:
• By the end of the conference, delegates will be able to;
• • Apply up to date evidence to inform clinical decisions;
• • Acquire practical skills by participating in interactive sessions;
• • Connect and collaborate with other delegates;
• • Consider strategies to ensure career longevity; and
• • Influence the future direction of Emergency Medicine in Canada

```html
<!DOCTYPE html>
<html lang="en">
<head>
<meta charset="utf-8">
<title>BRVO2020 Save the Date Postcard</title>
<link rel="stylesheet" href="https://fonts.googleapis.com/css2?family=Montserrat:ital,wght@0,400;0,500;0,600;0,700;0,800;1,700&display=swap">
<style>
  :root {
    --stage: #999999;
    --paper: #ffffff;
    --ink: #1e1e1e;
    --blue: #2aa6e0;
    --purple: #8e3a96;
    --violet: #6f55a8;
    --muted: #555555;
  }
  * { box-sizing: border-box; margin: 0; padding: 0; }
  html, body { width: 821px; height: 1200px; overflow: hidden; }
  body {
    background: var(--stage);
    font-family: "Montserrat", Arial, sans-serif;
    color: var(--ink);
    position: relative;
  }
  .card { position: absolute; left: 40px; width: 741px; background: var(--paper); overflow: hidden; }
  .card--front { top: 20px; height: 562px; }
  .card--back { top: 618px; height: 527px; }

  /* Front */
  .photo-strip { position: absolute; top: 0; left: 0; width: 741px; height: 234px; display: flex; gap: 3px; }
  .photo { flex: 1; height: 100%; }
  .photo--clinic { background: linear-gradient(135deg, #c9c3bd, #7d8791 60%, #3d4650); }
  .photo--canal { background: linear-gradient(180deg, #7fb5de 0%, #a7c4a0 38%, #4f7a45 62%, #3d6a7f 100%); }
  .photo--panel { background: linear-gradient(180deg, #b48a5a 0%, #8a6a4a 40%, #3a3a3a 75%, #1f1f1f 100%); }

  .date-box {
    position: absolute; left: 64px; top: 266px; width: 119px; height: 118px;
    border: 2px solid var(--ink);
    display: flex; flex-direction: column; align-items: center; justify-content: center;
  }
  .date-box__days { font-size: 50px; font-weight: 700; line-height: 1; letter-spacing: -1px; }
  .date-box__month { font-size: 25px; font-weight: 400; letter-spacing: 1px; margin-top: 4px; }

  .brand { display: flex; flex-direction: column; align-items: center; }
  .brand__row { display: flex; align-items: center; gap: 8px; }
  .brand__dot { width: 16px; height: 16px; border-radius: 50%; background: var(--blue); }
  .brand__name { font-weight: 800; color: var(--purple); }
  .brand__sub { color: var(--muted); font-weight: 500; }
  .brand--front { position: absolute; left: 268px; top: 300px; width: 200px; }
  .brand--front .brand__name { font-size: 30px; }
  .brand--front .brand__sub { font-size: 10px; margin-top: 4px; }

  .headline { font-weight: 700; color: var(--blue); line-height: 1.0; text-transform: uppercase; }
  .headline--front { position: absolute; left: 500px; top: 280px; width: 220px; text-align: center; font-size: 33px; }
  .tagline--front { position: absolute; left: 500px; top: 370px; width: 220px; text-align: center; font-size: 14px; font-weight: 500; }
  .tagline--front .dot { color: var(--purple); }

  .save-band {
    position: absolute; left: 0; top: 418px; width: 741px; height: 82px;
    background: linear-gradient(90deg, var(--purple), var(--violet) 45%, var(--blue));
    display: flex; align-items: center; justify-content: center;
    color: var(--paper); font-size: 52px; font-weight: 700; letter-spacing: 1px;
  }
  .url { letter-spacing: 3px; font-weight: 500; }
  .url--front { position: absolute; left: 0; top: 520px; width: 741px; height: 42px; display: flex; align-items: center; justify-content: center; font-size: 17px; }

  /* Back */
  .back-panel {
    position: absolute; left: 0; top: 0; width: 396px; height: 527px;
    background: linear-gradient(180deg, #3a8fc7 0%, #5577b3 45%, #8a48a0 100%);
    color: var(--paper); padding: 34px 0 0 55px;
  }
  .headline--back { color: var(--paper); font-size: 47px; line-height: 1.05; }
  .tagline--back { font-size: 19px; font-weight: 500; margin-top: 10px; word-spacing: 4px; }
  .objectives { margin-top: 26px; width: 300px; }
  .objectives__title { font-size: 17px; font-weight: 700; }
  .objectives__intro { font-size: 13px; line-height: 1.3; margin-top: 2px; }
  .objectives__list { list-style: none; margin-top: 12px; }
  .objectives__item { display: flex; gap: 10px; font-size: 13px; line-height: 1.3; margin-bottom: 14px; }
  .objectives__item svg { flex: none; width: 18px; height: 18px; margin-top: 1px; }

  .stamp { position: absolute; left: 604px; top: 41px; width: 91px; height: 91px; border: 2px dashed #777; }
  .brand--back { position: absolute; left: 440px; top: 88px; width: 150px; }
  .brand--back .brand__name { font-size: 19px; }
  .brand--back .brand__dot { width: 11px; height: 11px; }
  .brand--back .brand__sub { font-size: 7px; margin-top: 2px; }

  .address-lines { position: absolute; left: 436px; top: 208px; width: 260px; }
  .address-lines span { display: block; height: 31px; border-bottom: 1px dotted #555; }

  .vision { position: absolute; left: 436px; top: 376px; width: 275px; font-size: 13px; font-weight: 700; font-style: italic; line-height: 1.3; }
  .url--back { position: absolute; left: 436px; top: 458px; font-size: 14px; color: var(--blue); }
</style>
</head>
<body>
  <section class="card card--front">
    <div class="photo-strip">
      <div class="photo photo--clinic" role="img" aria-label="Photo of emergency medicine trainees practising a clinical skill"></div>
      <div class="photo photo--canal" role="img" aria-label="Photo of Ottawa canal with Parliament buildings"></div>
      <div class="photo photo--panel" role="img" aria-label="Photo of a conference panel session with audience"></div>
    </div>

    <div class="date-box">
      <div class="date-box__days">1-4</div>
      <div class="date-box__month">JUNE</div>
    </div>

    <div class="brand brand--front">
      <div class="brand__row"><span class="brand__dot"></span><span class="brand__name">BRVO2020</span></div>
      <div class="brand__sub">Ottawa June 1 - 4</div>
    </div>

    <h2 class="headline headline--front">Stronger Always</h2>
    <p class="tagline--front">Gather<span class="dot">.</span> Spark<span class="dot">.</span> Flourish<span class="dot">.</span></p>

    <div class="save-band">SAVE THE DATE</div>
    <p class="url url--front">brvosummitfold.ca</p>
  </section>

  <section class="card card--back">
    <div class="back-panel" role="img" aria-label="Blue to purple tinted photo of modern city architecture">
      <h2 class="headline headline--back">Stronger<br>Always</h2>
      <p class="tagline--back">Gather Spark Flourish</p>
      <div class="objectives">
        <p class="objectives__title">Learning Objectives:</p>
        <p class="objectives__intro">By the end of the conference, delegates will be able to;</p>
        <ul class="objectives__list">
          <li class="objectives__item"><svg viewBox="0 0 18 18"><circle cx="9" cy="9" r="7.5" fill="none" stroke="#fff" stroke-width="1.4"/><path d="M5 9l3 3 7-8" fill="none" stroke="#fff" stroke-width="1.6"/></svg><span>Apply up to date evidence to inform clinical decisions;</span></li>
          <li class="objectives__item"><svg viewBox="0 0 18 18"><circle cx="9" cy="9" r="7.5" fill="none" stroke="#fff" stroke-width="1.4"/><path d="M5 9l3 3 7-8" fill="none" stroke="#fff" stroke-width="1.6"/></svg><span>Acquire practical skills by participating in interactive sessions;</span></li>
          <li class="objectives__item"><svg viewBox="0 0 18 18"><circle cx="9" cy="9" r="7.5" fill="none" stroke="#fff" stroke-width="1.4"/><path d="M5 9l3 3 7-8" fill="none" stroke="#fff" stroke-width="1.6"/></svg><span>Connect and collaborate with other delegates;</span></li>
          <li class="objectives__item"><svg viewBox="0 0 18 18"><circle cx="9" cy="9" r="7.5" fill="none" stroke="#fff" stroke-width="1.4"/><path d="M5 9l3 3 7-8" fill="none" stroke="#fff" stroke-width="1.6"/></svg><span>Consider strategies to ensure career longevity; and</span></li>
          <li class="objectives__item"><svg viewBox="0 0 18 18"><circle cx="9" cy="9" r="7.5" fill="none" stroke="#fff" stroke-width="1.4"/><path d="M5 9l3 3 7-8" fill="none" stroke="#fff" stroke-width="1.6"/></svg><span>Influence the future direction of Emergency Medicine in Canada</span></li>
        </ul>
      </div>
    </div>

    <div class="stamp"></div>
    <div class="brand brand--back">
      <div class="brand__row"><span class="brand__dot"></span><span class="brand__name">BRVO2020</span></div>
      <div class="brand__sub">Ottawa June 1 - 4</div>
    </div>

    <div class="address-lines"><span></span><span></span><span></span><span></span><span></span></div>

    <p class="vision">The vision of the BRVO 2020 conference is to improve patient care by bringing together the Canadian Emergency Medicine community.</p>
    <p class="url url--back">brvosummitfold.ca</p>
  </section>
</body>
</html>
```